R. K. Dalby, CPA & Associates, LLC
Your Accounting, Finance, and Tax Specialist
R. K. Dalby, CPA & Associates, LLC -
Use specific fonts
open to fonts
Professional
Rennick K. Dalby, CPA
President
4718 Copper Wren Ave. West Palm Beach, FL 33952
rennickdalbycpa@mailnook.test

```html
<!DOCTYPE html>
<html lang="en">
<head>
<meta charset="utf-8">
<title>R. K. Dalby, CPA &amp; Associates, LLC — Business Cards</title>
<link rel="stylesheet" href="https://fonts.googleapis.com/css2?family=Open+Sans:wght@400;700&family=Tinos:wght@400&display=swap">
<style>
  :root {
    --magenta: #a0266e;
    --magenta-dark: #6d1249;
    --magenta-light: #c64a92;
    --silver: #b9b9bd;
    --ink: #2a2a2a;
    --card-light: #ffffff;
    --card-dark: #111111;
    --backdrop: #e9e6e2;
    --text-on-dark: #e8e8e8;
  }
  * { box-sizing: border-box; margin: 0; padding: 0; }
  html, body { width: 1200px; height: 852px; overflow: hidden; }
  body { background: var(--backdrop); position: relative; font-family: "Tinos", serif; }

  .card {
    position: absolute;
    width: 600px; height: 340px;
    border-radius: 18px;
    overflow: hidden;
    box-shadow: 0 6px 18px rgba(0,0,0,0.18);
  }
  .card--light { left: 120px; top: 80px; background: var(--card-light); color: var(--ink); }
  .card--dark  { left: 480px; top: 432px; background: var(--card-dark); color: var(--text-on-dark); }

  .card__band { position: absolute; inset: 0; width: 100%; height: 100%; }

  .card__holder {
    position: absolute; right: 30px; top: 20px; text-align: right;
    font-family: "Open Sans", sans-serif; color: #fff;
  }
  .card__holder-name { font-size: 19px; font-weight: 700; }
  .card__holder-title { font-size: 13px; font-weight: 700; margin-top: 2px; }

  .brand {
    position: absolute; left: 30px; top: 142px; width: 200px;
    display: flex; align-items: center; gap: 12px;
  }
  .brand__mark { width: 40px; height: 40px; background: var(--magenta); flex: none; }
  .brand__text { width: 148px; }
  .brand__name {
    font-family: "Tinos", serif; font-weight: 400;
    font-size: 18px; line-height: 1.15; color: var(--magenta);
  }
  .card--dark .brand__name { color: var(--magenta-light); }

  .divider {
    position: absolute; left: 244px; top: 128px; width: 1px; height: 100px;
    background: var(--silver);
  }
  .brand__tagline {
    position: absolute; left: 260px; top: 130px; width: 300px;
    font-family: "Open Sans", sans-serif; font-size: 11px; color: #777;
  }
  .card--dark .brand__tagline { color: #aaa; }

  .contact { position: absolute; left: 260px; top: 166px; list-style: none; }
  .contact__item { display: flex; align-items: center; gap: 8px; font-size: 15px; line-height: 22px; }
  .contact__icon { width: 13px; height: 13px; flex: none; }

  .address {
    position: absolute; left: 30px; top: 250px; width: 200px; text-align: right;
    font-size: 15px; line-height: 20px;
  }
</style>
</head>
<body>

<article class="card card--light">
  <svg class="card__band" viewBox="0 0 600 340" aria-hidden="true">
    <defs>
      <linearGradient id="bandLight" x1="0" y1="0" x2="1" y2="0">
        <stop offset="0" stop-color="var(--magenta-light)"/>
        <stop offset="1" stop-color="var(--magenta-dark)"/>
      </linearGradient>
    </defs>
    <path d="M0 0 H600 V70 C420 70 250 92 0 112 Z" fill="url(#bandLight)"/>
    <path d="M0 112 C250 92 420 70 600 70 V82 C420 82 250 100 0 122 Z" fill="var(--silver)"/>
    <path d="M600 300 C520 318 440 330 380 340 H600 Z" fill="url(#bandLight)"/>
  </svg>
  <div class="card__holder">
    <p class="card__holder-name">Rennick K. Dalby, CPA</p>
    <p class="card__holder-title">President</p>
  </div>
  <div class="brand">
    <span class="brand__mark"></span>
    <div class="brand__text"><p class="brand__name">R. K. Dalby, CPA &amp; Associates, LLC</p></div>
  </div>
  <span class="divider"></span>
  <p class="brand__tagline">Your Accounting, Finance, and Tax Specialist</p>
  <ul class="contact">
    <li class="contact__item"><svg class="contact__icon" viewBox="0 0 12 12"><rect x="3" y="0.5" width="6" height="11" rx="1.2" fill="var(--magenta)"/></svg>561.555.0139</li>
    <li class="contact__item"><svg class="contact__icon" viewBox="0 0 12 12"><path d="M2 1 L4.5 1 L5.5 4 L4 5 C4.8 6.8 5.6 7.6 7 8 L8 6.5 L11 7.5 L11 10 C6 11 1 6 2 1 Z" fill="var(--magenta)"/></svg>561.555.0172</li>
    <li class="contact__item"><svg class="contact__icon" viewBox="0 0 12 12"><circle cx="6" cy="6" r="5.5" fill="var(--magenta)"/></svg>rennickdalbycpa@mailnook.test</li>
  </ul>
  <p class="address">4718 Copper Wren Ave.<br>West Palm Beach, FL 33952</p>
</article>

<article class="card card--dark">
  <svg class="card__band" viewBox="0 0 600 340" aria-hidden="true">
    <defs>
      <linearGradient id="bandDark" x1="0" y1="0" x2="1" y2="0">
        <stop offset="0" stop-color="var(--magenta-light)"/>
        <stop offset="1" stop-color="var(--magenta-dark)"/>
      </linearGradient>
    </defs>
    <path d="M0 0 H600 V70 C420 70 250 92 0 112 Z" fill="url(#bandDark)"/>
    <path d="M0 112 C250 92 420 70 600 70 V82 C420 82 250 100 0 122 Z" fill="var(--silver)"/>
    <path d="M600 300 C520 318 440 330 380 340 H600 Z" fill="url(#bandDark)"/>
  </svg>
  <div class="card__holder">
    <p class="card__holder-name">Rennick K. Dalby, CPA</p>
    <p class="card__holder-title">President</p>
  </div>
  <div class="brand">
    <span class="brand__mark"></span>
    <div class="brand__text"><p class="brand__name">R. K. Dalby, CPA &amp; Associates, LLC</p></div>
  </div>
  <span class="divider"></span>
  <p class="brand__tagline">Your Accounting, Finance, and Tax Specialist</p>
  <ul class="contact">
    <li class="contact__item"><svg class="contact__icon" viewBox="0 0 12 12"><rect x="3" y="0.5" width="6" height="11" rx="1.2" fill="var(--magenta-light)"/></svg>561.555.0139</li>
    <li class="contact__item"><svg class="contact__icon" viewBox="0 0 12 12"><path d="M2 1 L4.5 1 L5.5 4 L4 5 C4.8 6.8 5.6 7.6 7 8 L8 6.5 L11 7.5 L11 10 C6 11 1 6 2 1 Z" fill="var(--magenta-light)"/></svg>561.555.0172</li>
    <li class="contact__item"><svg class="contact__icon" viewBox="0 0 12 12"><circle cx="6" cy="6" r="5.5" fill="var(--magenta-light)"/></svg>rennickdalbycpa@mailnook.test</li>
  </ul>
  <p class="address">4718 Copper Wren Ave.<br>West Palm Beach, FL 33952</p>
</article>

</body>
</html>
```